Welding and farication business card

Business name Tbm Welding & Fabrication

I need a business card made for my welding and fabrication business that is bold and stands out. My business is both welding repairs on machinery and anything else you can imagine as well as fabricating new products. i have used this service before and was very happy with the out come of my design logo. i think the card should remain fairly simple and classy but also be bold. I think a black card would best be suited to the talk with my logo on it. i feel the back of the card should just have my logo and the front have my logo email, website and phone number and maybe incorporate a facebook and instagram simple if it can be made look good these arnt a necessity.
I have included both my logo and some business card ideas below

Target Market(s)

Farmers, heavy industry, earthmoving, trucking

Industry/Entity Type

Engineering

Contact Information for Business Card

0491570156
dale@tbmweldingfab.example
www.tbmweldingfab.example

Colors
33a6d7
0255a3

Requirements
Must have
• Dale Hutchins
my phone number 0491570156
my logo
Preferably a black card desgn
Nice to have
• List of what i do,
Sheds and carports
Ute trays
Stockyards
Trailers
Farm equipment
Stockcrates
Gateways and Entrances
Breakdowns
Maintenance
And lots more!

```html
<!DOCTYPE html>
<html lang="en">
<head>
<meta charset="utf-8">
<title>Tbm Welding &amp; Fabrication – Business Card</title>
<link href="https://fonts.googleapis.com/css2?family=Montserrat:ital,wght@0,400;0,700;0,800;1,800&display=swap" rel="stylesheet">
<style>
  :root {
    --bg: #e9e7e3;
    --card-black: #000000;
    --white: #ffffff;
    --slate: #4b5a6b;
    --slate-text: #4a5668;
    --brand-blue: #0255a3;
    --faint: #3a3f46;
  }
  * { margin: 0; padding: 0; box-sizing: border-box; }
  html, body { width: 1200px; height: 800px; overflow: hidden; }
  body {
    background: var(--bg);
    font-family: "Montserrat", Arial, sans-serif;
    position: relative;
  }
  .card {
    position: absolute;
    left: 341px;
    width: 589px;
    height: 336px;
    background: var(--card-black);
    overflow: hidden;
  }
  .card--front { top: 35px; }
  .card--back { top: 420px; }

  /* Front */
  .logo-band {
    position: absolute; left: 0; top: 0; bottom: 0; width: 90px;
    background: var(--white);
    display: flex; align-items: center; justify-content: center;
  }
  .logo-band__name {
    transform: rotate(-90deg);
    font-weight: 800; font-size: 62px; letter-spacing: 2px;
    color: var(--brand-blue); white-space: nowrap;
  }
  .owner-name {
    position: absolute; left: 122px; top: 92px;
    font-weight: 700; font-size: 47px; letter-spacing: -0.5px;
    color: var(--slate-text); white-space: nowrap; line-height: 1;
  }
  .phone {
    position: absolute; right: 72px; top: 129px;
    font-weight: 700; font-size: 40px; color: var(--white);
    line-height: 1; letter-spacing: -0.5px;
  }
  .contact {
    position: absolute; right: 69px; top: 184px;
    text-align: right; color: var(--white);
    font-size: 17.5px; line-height: 24px;
  }
  .tagline {
    position: absolute; right: -146px; top: 152px;
    width: 310px; text-align: center;
    transform: rotate(-90deg);
    font-weight: 800; font-style: italic; font-size: 21px; line-height: 26px;
    color: var(--white); white-space: nowrap;
  }

  /* Back */
  .services-band {
    position: absolute; left: 0; top: 0; bottom: 0; width: 91px;
    background: var(--slate);
  }
  .services-band__title {
    position: absolute; left: 89px; top: 18px;
    transform-origin: 0 0; transform: rotate(90deg);
    font-weight: 700; font-size: 32px; color: var(--white);
    white-space: nowrap; line-height: 1;
  }
  .services-list {
    position: absolute; left: 122px; top: 12px;
    list-style: none; color: var(--white);
    font-size: 17.4px; line-height: 22.5px;
  }
  .services-list strong { font-weight: 800; }
  .services-more {
    position: absolute; left: 121px; top: 216px;
    font-weight: 800; font-size: 41px; line-height: 39px;
    color: var(--slate-text);
  }
  .back-mark {
    position: absolute; right: 24px; bottom: 26px;
    font-weight: 800; font-size: 50px; letter-spacing: 2px;
    color: var(--faint);
  }
</style>
</head>
<body>
  <section class="card card--front" aria-label="Front of card">
    <div class="logo-band"><span class="logo-band__name">TBM</span></div>
    <h1 class="owner-name">DALE HUTCHINS</h1>
    <p class="phone">0491570156</p>
    <p class="contact">
      www.tbmweldingfab.example<br>
      dale@tbmweldingfab.example
    </p>
    <p class="tagline">WELDING &amp; FABRICATION</p>
  </section>

  <section class="card card--back" aria-label="Back of card">
    <div class="services-band"><h2 class="services-band__title">MY Services</h2></div>
    <ul class="services-list">
      <li>Sheds and carports</li>
      <li>Ute trays</li>
      <li>Stock<strong>YARDS</strong></li>
      <li>Trailers</li>
      <li><strong>FARM EQUIPMENT</strong></li>
      <li>Stockcrates</li>
      <li><strong>Gateways</strong> and Entrances</li>
      <li><strong>BREAK</strong>downs</li>
      <li>Maintenance</li>
    </ul>
    <p class="services-more">AND<br>LOTS<br>MORE</p>
    <span class="back-mark">TBM</span>
  </section>
</body>
</html>
```